Architectural Design practice needs new logo /letterhead design

We need a new logo / letterhead design to freshen up the practice image. We are an architects practice working in all building design sectors and want a new modern fresh logo / letterhead but retaining a professional feel, so not too gimmicky. The current branding colour palette uses blue and grey, which we still like, but we are also open to other suggestions. I have attached our current letterhead which has served us well and incorporates the FENC logo, but this was produced in-house using only Word when we first started the business and we would now like a new more modern and professional design.
Possibly include the acronym KPT , or kpt, second file added shows an attempt I did myself, which is a bit basic but gives an idea of the type of thing we are looking for

File added showing the type of thing we are looking for

Building

Sans Serif

```html
<!DOCTYPE html>
<html lang="en">
<head>
<meta charset="utf-8">
<title>K Pryor Turner Associates – Letterhead</title>
<link href="https://fonts.googleapis.com/css2?family=Questrial&display=swap" rel="stylesheet">
<style>
  :root {
    --brand-blue: #2a4bcc;
    --rule-grey: #6b6b6b;
    --paper: #ffffff;
    --backdrop: #e4e4e4;
    --ink-light: #ffffff;
  }
  * { margin: 0; padding: 0; box-sizing: border-box; }
  html, body {
    width: 1200px;
    height: 1121px;
    overflow: hidden;
    background: var(--backdrop);
    font-family: "Questrial", "Century Gothic", sans-serif;
  }
  .letterhead {
    position: absolute;
    left: 244px;
    top: 84px;
    width: 656px;
    height: 930px;
    background: var(--paper);
    box-shadow: 0 2px 8px rgba(0,0,0,0.25);
  }
  .letterhead__header {
    position: absolute;
    left: 0; top: 0;
    width: 100%;
    height: 160px;
    background: var(--brand-blue);
    border-bottom: 5px solid var(--rule-grey);
  }
  .brand-mark {
    position: absolute;
    left: 0; top: 0;
    width: 86px;
    height: 155px;
    background: var(--paper);
    display: flex;
    flex-direction: column;
    align-items: center;
    justify-content: flex-end;
    padding-bottom: 34px;
    gap: 8px;
  }
  .brand-mark__square {
    width: 14px;
    height: 14px;
    background: var(--brand-blue);
  }
  .brand-mark__name {
    font-size: 32px;
    color: var(--brand-blue);
    letter-spacing: 0.5px;
    line-height: 1;
  }
  .header-frame {
    position: absolute;
    left: 110px;
    top: 17px;
    width: 517px;
    height: 119px;
    border: 1px solid rgba(255,255,255,0.85);
    color: var(--ink-light);
  }
  .practice-name {
    position: absolute;
    left: 0; right: 40px;
    top: 4px;
    text-align: center;
    font-size: 33px;
    font-weight: 400;
    line-height: 1.1;
  }
  .practice-role {
    position: absolute;
    left: 0; right: 40px;
    top: 40px;
    text-align: center;
    font-size: 17.5px;
    letter-spacing: 0.3px;
  }
  .practice-address {
    position: absolute;
    left: 0; right: 0;
    top: 73px;
    text-align: right;
    padding-right: 4px;
    font-size: 10.5px;
    word-spacing: 1px;
    white-space: nowrap;
  }
  .practice-contact {
    position: absolute;
    left: 66px;
    top: 93px;
    display: flex;
    gap: 10px;
    font-size: 11.5px;
    white-space: nowrap;
  }
  .contact-item {
    display: flex;
    align-items: center;
    gap: 4px;
  }
  .contact-item svg { display: block; }
</style>
</head>
<body>
  <article class="letterhead">
    <header class="letterhead__header">
      <div class="brand-mark">
        <span class="brand-mark__square"></span>
        <span class="brand-mark__name">KPT</span>
      </div>
      <div class="header-frame">
        <h1 class="practice-name">K Pryor Turner Associates</h1>
        <p class="practice-role">CHARTERED ARCHITECTS</p>
        <p class="practice-address">K Pryor Turner Associates Ltd,&nbsp; Linden House,&nbsp; 42 Harrow Road,&nbsp; Alderley,&nbsp; Westshire,&nbsp; AL4 2QN</p>
        <div class="practice-contact">
          <span class="contact-item">
            <svg width="14" height="11" viewBox="0 0 14 11" aria-hidden="true">
              <path d="M1 3.5 Q7 -0.5 13 3.5 L11 5 L9.5 3.5 H4.5 L3 5 Z" fill="#fff"/>
              <rect x="3.5" y="5" width="7" height="5" rx="1" fill="#fff"/>
            </svg>
            01632 960418
          </span>
          <span class="contact-item">
            <svg width="12" height="11" viewBox="0 0 12 11" aria-hidden="true">
              <rect x="0.5" y="2" width="11" height="8.5" rx="1.5" fill="none" stroke="#fff"/>
              <rect x="3" y="0.5" width="6" height="3" fill="#fff"/>
              <line x1="3" y1="6" x2="9" y2="6" stroke="#fff"/>
              <line x1="3" y1="8" x2="9" y2="8" stroke="#fff"/>
            </svg>
            01632 960427
          </span>
          <span class="contact-item">
            <svg width="15" height="11" viewBox="0 0 15 11" aria-hidden="true">
              <rect x="0.5" y="0.5" width="14" height="10" fill="none" stroke="#fff"/>
              <polyline points="0.5,0.5 7.5,6 14.5,0.5" fill="none" stroke="#fff"/>
            </svg>
            enquiry@kptassociates.co.uk
          </span>
        </div>
      </div>
    </header>
  </article>
</body>
</html>
```